revised: 'wexford joinery' logo -or- business card

we require a business card or a logo that can be used on a business card & other stationery

(i've just recently decided to open this contest up to logo designs as well - but if you have already been working on a card concept, please feel free to continue with it & submit!)

-

We design and build custom brackets and fixings for our customers and their castles, i.e. homes, offices, workshops, farms etc. Our products might be used to:
- brace or support structures, such as houses, decks, small bridges, etc.
- connect any building material to another
- or could simply be a unique piece that exists as a talking point

As part of our design process we would produce drawings/plans/blue prints/prototypes of the product. Our designs factor in multiple elements, from the materials being joined, the client's taste, and the overall durability demanded by the application - if necessary, the bracket may also be endorsed by a third party, such as a stuctural or mechanical engineer.

The build process takes part in our workshop and on the client's site - some elements may be manufactured off-site, depending on the design chosen and the materials used.

Our brackets are designed to our customers' tastes and could be made to be hidden within the structure or exposed to create interest. Our brackets can be large or small, or be neat with clean lines or take on more of an industrial look.
Updates

please note brief has been updated with a more specific description of our business activity

i have also added the final drawing that was used to water-jet the bracket shown in the photos

also, you will note i changed the title to 'logo + business card'

i don't expect a logo as a discrete artefact of the job, however, i expect that some or all elements on the face of the business card will lend themselves to the street sign (as stated in the original brief) as well as any future logo used on letter heads, invoices, etcetera

another update - changed the allowable entries to include logo's only, as well as business cards

Industry/Entity Type

Industrial

Requirements
Must have
• the face should have the name 'Wexford Joinery' (or no/all-caps)

the number '75' in the logo, which will also be turned into a conservative (residential) street sign ('75' being a street number) - '75' should stand alone -OR- be readily identified by someone who has previously received a business card

i need to make this '75' and any associated 'framing', so it should be transferrable to cad/dxf for machining, laser/water-cutting, brazing/welding, etcet.

(on that note, the winning designer will be able to share their vision for this sign and we'll adhere to it ... within the realms of possibility! if you're happy with the result then you could include it in your portfolio)
Nice to have
• one side of the card needs a majority of space for quotes, hand-written information, etcet. so this side should be white or a light, complimentary colour suitable for black/blue pen

the following should appear somewhere on the card (there is no email or website) :
- name : Mara Quell (Proprietor)
- mobile phone number : +61 (0) 498 716203
- abn: 58 604 917 235

any combination of the following (or equivalent) text:

* 'your castle' - this is slang for your house/place (i prefer this to 'home' as 1: it can apply to a place of business, and 2: for me at least, it conjurs images of wrought iron, brass, hardwood & stone)

* unique

* ...

```html
<!DOCTYPE html>
<html lang="en">
<head>
<meta charset="utf-8">
<title>Wexford Joinery — Business Card</title>
<link rel="stylesheet" href="https://fonts.googleapis.com/css2?family=Arimo:wght@400;700&display=swap">
<style>
  :root {
    --page: #ffffff;
    --card: #ffffff;
    --card-edge: #9a9a9a;
    --ink: #111111;
    --ink-soft: #2a2a2a;
    --muted: #b5b5b5;
    --ghost: #ececec;
  }
  * { box-sizing: border-box; margin: 0; padding: 0; }
  html, body {
    width: 845px;
    height: 1200px;
    overflow: hidden;
    background: var(--page);
    font-family: "Arimo", Arial, sans-serif;
    color: var(--ink);
  }
  .sheet { position: relative; width: 845px; height: 1200px; }

  .card {
    position: absolute;
    left: 182px;
    width: 490px;
    height: 318px;
    background: var(--card);
    border: 1px solid var(--card-edge);
    overflow: hidden;
  }
  .card--front { top: 254px; }
  .card--back  { top: 656px; }

  .card__rule {
    position: absolute;
    left: 69px;
    top: 0;
    width: 2px;
    height: 100%;
    background: var(--ink);
  }

  .brand-dot {
    position: absolute;
    left: 36px;
    top: 58px;
    width: 68px;
    height: 68px;
    border: 2px solid var(--ink);
    border-radius: 50%;
    background: var(--card);
  }

  .brand {
    position: absolute;
    left: 135px;
    top: 79px;
  }
  .brand__name {
    font-weight: 700;
    font-size: 24px;
    letter-spacing: 0.1px;
    color: var(--ink);
    line-height: 1;
  }
  .brand__tagline {
    margin-top: 8px;
    font-size: 14.5px;
    color: var(--muted);
    line-height: 1;
  }

  .contact {
    position: absolute;
    left: 135px;
    top: 191px;
    color: var(--ink-soft);
  }
  .contact__name {
    font-size: 17.5px;
    line-height: 1;
  }
  .contact__role { font-size: 13px; }
  .contact__details {
    margin-top: 14px;
    font-size: 15px;
    line-height: 20px;
  }

  .card__ghost {
    position: absolute;
    left: 0;
    top: 0;
    width: 100%;
    height: 100%;
  }
</style>
</head>
<body>
  <main class="sheet">
    <section class="card card--front" aria-label="Business card front">
      <div class="card__rule"></div>
      <div class="brand-dot" aria-hidden="true"></div>
      <div class="brand">
        <h1 class="brand__name">Wexford Joinery</h1>
        <p class="brand__tagline">Bespoke Bracket Manufacturing Service</p>
      </div>
      <div class="contact">
        <p class="contact__name">Mara Quell <span class="contact__role">(Proprietor)</span></p>
        <p class="contact__details">Mobile : +61 (0) 498 716203<br>Abn: 58 604 917 235</p>
      </div>
    </section>

    <section class="card card--back" aria-label="Business card back, space for notes">
      <svg class="card__ghost" viewBox="0 0 490 318" aria-hidden="true">
        <circle cx="311" cy="165" r="205" fill="none" stroke="var(--ghost)" stroke-width="13"/>
      </svg>
      <div class="card__rule"></div>
    </section>
  </main>
</body>
</html>
```